QMR Design

Looking for the website design of an small business,
The company is newly established. The Company Trades with Steel from Asiam Europe to Australia and New Zealand.

In the main Page, we would like to have a video showing the process of how steel is made(or the iron melt, pipe rolled, etc)

We would like to show pictures of the Products we trade and an table with some information about the specifications and Product.

About the company,
Industry is Iron and Steel
The company source and supply various steel and metal products within our international network also manage all aspects of the supply process from point of manufacture to point of delivery. the goal is to create value within the supply chain by building strong supplier, customers and service providers, funding of both customers and suppliers, experienced risk management, efficient document handling.
Main products: LSAW pipe, ERW Pipe, Flat rolled Products (such is Steel Coil, Aluminium Zinc Coil, Floor Plate, Plate, etc), Reinforcing bar

Number of Pages Required

5+ page

Font styles to use
Sans Serif

Requirements
Must have
• Video in the home page showing

```html
<!DOCTYPE html>
<html lang="en">
<head>
<meta charset="utf-8">
<title>QMR – Steel Trading</title>
<link href="https://fonts.googleapis.com/css2?family=Poppins:wght@500;600;700;800&family=Inter:wght@400;500;600&display=swap" rel="stylesheet">
<style>
:root{
  --orange:#f04e23;
  --navy:#1b2a4a;
  --ink:#222;
  --muted:#555;
  --soft:#f4f1ef;
  --dark:#1c1c1e;
  --line:#e3e3e3;
}
*{box-sizing:border-box;margin:0;padding:0}
html,body{width:1200px;height:4199px;overflow:hidden;background:#fff}
body{font-family:Inter,sans-serif;color:var(--ink);position:relative}
.btn{position:absolute;display:flex;align-items:center;justify-content:center;background:var(--orange);color:#fff;font-family:Poppins,sans-serif;font-weight:600;letter-spacing:.3px}
.photo{position:absolute}
.sec-title{position:absolute;left:0;width:1200px;text-align:center;font-family:Poppins,sans-serif;font-weight:700;color:var(--navy);font-size:26px}
.sec-rule{position:absolute;left:575px;width:50px;height:3px;background:var(--orange)}

/* header */
.site-header{position:absolute;top:0;left:0;width:1200px;height:118px;background:#fff}
.brand{position:absolute;left:130px;top:38px;display:flex;align-items:center;gap:10px;font-family:Poppins,sans-serif;font-weight:800;font-size:34px;color:var(--navy)}
.brand i{width:22px;height:22px;background:var(--orange);border-radius:50%;display:block}
.search{position:absolute;left:518px;top:26px;width:240px;height:36px;border:1px solid #bbb;font-size:11px;color:#444;padding:11px 14px}
.search svg{position:absolute;right:10px;top:10px}
.call{position:absolute;left:785px;top:26px}
.call small{position:absolute;left:37px;top:0;font-size:11px;font-weight:600;width:60px}
.call b{position:absolute;left:37px;top:13px;font-size:20px;font-weight:500;color:var(--navy);white-space:nowrap}
.cart{position:absolute;left:978px;top:30px;font-size:11px;color:#444}
.cart span{position:absolute;left:0;top:12px;white-space:nowrap}
.cart svg{position:absolute;left:46px;top:0}
.cart em{position:absolute;left:72px;top:-6px;width:16px;height:16px;background:var(--orange);border-radius:50%;color:#fff;font-style:normal;font-size:10px;text-align:center;line-height:16px}
.nav{position:absolute;top:86px;left:0;font-size:14px;font-weight:500}
.nav a{position:absolute;white-space:nowrap;color:var(--ink);text-decoration:none}
.nav a.on{color:var(--orange)}

/* hero */
.hero{position:absolute;top:118px;left:0;width:1200px;height:555px;background:linear-gradient(160deg,#4a4644 0%,#6e6862 35%,#3a3836 60%,#7a716a 85%,#2e2c2b 100%)}
.hero h1{position:absolute;top:166px;width:1200px;text-align:center;font-family:Poppins,sans-serif;font-weight:700;color:#fff;font-size:46px}
.hero p{position:absolute;top:232px;width:1200px;text-align:center;color:#fff;font-family:Poppins,sans-serif;font-weight:600;font-size:17px}
.dots{position:absolute;top:493px;left:557px;display:flex;gap:12px;align-items:center}
.dots i{width:7px;height:7px;border-radius:50%;background:#fff;display:block}
.dots i.on{width:11px;height:11px;border:2px solid #fff;background:var(--orange)}

/* products */
.product{position:absolute;width:458px;height:333px;background:linear-gradient(135deg,#2f3035,#6c6f74 50%,#3a3b40)}
.product::after{content:"";position:absolute;left:0;right:0;bottom:0;height:110px;background:linear-gradient(transparent,rgba(0,0,0,.65))}
.product h3{position:absolute;left:20px;bottom:38px;z-index:1;color:#fff;font-family:Poppins,sans-serif;font-weight:600;font-size:18px}
.product p{position:absolute;left:20px;bottom:20px;z-index:1;color:#fff;font-size:13px}
.product .btn{right:20px;bottom:20px;width:102px;height:34px;font-size:14px;z-index:1}

/* welcome */
.welcome{position:absolute;top:1533px;left:0;width:1200px;height:453px;background:var(--soft)}
.welcome h2{position:absolute;left:132px;top:60px;font-family:Poppins,sans-serif;font-weight:700;font-size:25px;color:var(--navy)}
.welcome h2::after{content:"";position:absolute;left:0;top:44px;width:48px;height:3px;background:var(--orange)}
.welcome p{position:absolute;left:132px;top:138px;width:350px;font-size:14.5px;line-height:22.4px;color:#333}
.video{position:absolute;left:528px;top:44px;width:540px;height:366px;background:linear-gradient(120deg,#2b3036,#8d8f92 45%,#c9b36a 75%,#3a3e44)}
.video svg{position:absolute;left:233px;top:146px}

/* steel trading */
.trading{position:absolute;top:1986px;left:0;width:1200px;height:442px;background:linear-gradient(100deg,#1d1d1f,#2b2b2d 50%,#1a1a1b)}
.trading h2{position:absolute;top:80px;width:1200px;text-align:center;color:#fff;font-family:Poppins,sans-serif;font-weight:700;font-size:38px}
.trading p{position:absolute;top:180px;width:1200px;text-align:center;color:#eee;font-size:20px;line-height:28px}

/* specs */
.tabs{position:absolute;top:2561px;left:0;font-size:11.5px}
.tab{position:absolute;height:38px;border:1px solid #aaa;display:flex;align-items:center;justify-content:center;color:#333;background:#fff}
.tab.on{background:var(--orange);border-color:var(--orange);color:#fff;font-weight:600}
.spec{position:absolute;left:137px;top:2630px;width:931px;border-collapse:collapse;font-size:13px;box-shadow:0 4px 14px rgba(0,0,0,.08);background:#fff}
.spec th{background:#5d5d5f;color:#fff;height:47px;font-family:Poppins,sans-serif;font-weight:600;font-size:12px;border-right:1px solid #777}
.spec td{height:41.6px;text-align:center;border-right:1px solid var(--line);border-bottom:1px solid var(--line);color:#333}
.spec th:first-child{text-align:left;padding-left:40px}
.spec td:first-child{text-align:left;padding-left:36px}
.spec td:last-child,.spec th:last-child{border-right:none}

/* blog */
.blog{position:absolute;top:3057px;left:0;width:1200px;height:554px;background:var(--soft)}
.post{position:absolute;top:134px;width:298px;height:375px;background:#fff}
.post .photo{left:0;top:0;width:298px;height:187px}
.post h4{position:absolute;left:22px;top:213px;width:260px;font-family:Poppins,sans-serif;font-weight:600;font-size:12px;line-height:17px;color:#222}
.post p{position:absolute;left:22px;top:256px;width:250px;font-size:11.5px;line-height:17px;color:#555}
.post .btn{left:22px;top:322px;width:86px;height:27px;font-size:10px}

/* cta */
.cta{position:absolute;top:3611px;left:0;width:1200px;height:242px;background:linear-gradient(110deg,#0f2a6b,#1d4aa8 40%,#0c2258 70%,#1a3f94)}
.cta h2{position:absolute;left:132px;top:76px;width:620px;white-space:nowrap;color:#fff;font-family:Poppins,sans-serif;font-weight:600;font-size:23px;line-height:33px}

/* footer */
.footer{position:absolute;top:3853px;left:0;width:1200px;height:346px;background:var(--dark);color:#ccc}
.footer .brand{left:128px;top:106px;color:#fff;font-size:34px}
.footer h5{position:absolute;top:50px;font-family:Poppins,sans-serif;font-weight:600;font-size:12px;color:#fff}
.fmenu{position:absolute;left:424px;top:87px;list-style:none;font-size:11.5px;line-height:19.6px}
.fitem{position:absolute;font-size:11.5px;line-height:15px;color:#ccc}
.fitem i{position:absolute;left:-34px;top:2px;width:24px;height:24px;border-radius:50%;background:#fff;display:flex;align-items:center;justify-content:center}
.footer hr{position:absolute;left:132px;top:286px;width:936px;border:none;border-top:1px solid #333}
.copy{position:absolute;top:305px;width:1200px;text-align:center;font-size:11px;color:#bbb}
</style>
</head>
<body>

<header class="site-header">
  <div class="brand"><i></i>QMR</div>
  <div class="search">SEARCH
    <svg width="13" height="13" viewBox="0 0 13 13" fill="none" stroke="#555" stroke-width="1.5"><circle cx="5.5" cy="5.5" r="4"/><path d="M8.5 8.5l3.5 3.5"/></svg>
  </div>
  <div class="call">
    <svg width="28" height="28" viewBox="0 0 24 24" fill="none" stroke="#1b2a4a" stroke-width="1.6"><path d="M5 3h4l2 5-2.5 1.5a11 11 0 0 0 6 6L16 13l5 2v4a2 2 0 0 1-2 2A17 17 0 0 1 3 5a2 2 0 0 1 2-2z"/></svg>
    <small>CALL US</small><b>555.014.2290</b>
  </div>
  <div class="cart"><span>MY CART</span>
    <svg width="32" height="28" viewBox="0 0 32 28" fill="none" stroke="#444" stroke-width="1.6"><path d="M1 2h5l4 16h16l4-12H8"/><circle cx="12" cy="24" r="2"/><circle cx="24" cy="24" r="2"/></svg>
    <em>0</em>
  </div>
  <nav class="nav">
    <a class="on" style="left:520px">HOME</a>
    <a style="left:598px">ABOUT US</a>
    <a style="left:706px">PRODUCTS</a>
    <a style="left:810px">SERVICES</a>
    <a style="left:913px">BLOG</a>
    <a style="left:983px">CONTACT US</a>
  </nav>
</header>

<section class="hero" role="img" aria-label="Close-up photograph of stacked steel reinforcing bars">
  <h1>REINFORCING BAR</h1>
  <p>LOREM IPSUM IS SIMPLY DUMMY TEXT OF THE PRINTING</p>
  <a class="btn" style="left:531px;top:280px;width:137px;height:42px;font-size:16px">READ MORE</a>
  <div class="dots"><i></i><i></i><i class="on"></i><i></i><i></i></div>
</section>

<h2 class="sec-title" style="top:710px">OUR PRODUCTS</h2>
<div class="sec-rule" style="top:757px"></div>

<article class="product" style="left:132px;top:797px" role="img" aria-label="Photograph of stacked LSAW steel pipes in a warehouse">
  <h3>LSAW PIPE</h3><p>Lorem Ipsum is simply dummy text</p><a class="btn">SHOP NOW</a>
</article>
<article class="product" style="left:610px;top:797px;background:linear-gradient(135deg,#3a2f28,#8a6a50 50%,#2e2a28)" role="img" aria-label="Photograph of stacked ERW steel pipes">
  <h3>ERW PIPE</h3><p>Lorem Ipsum is simply dummy text</p><a class="btn">SHOP NOW</a>
</article>
<article class="product" style="left:132px;top:1151px;background:linear-gradient(135deg,#4a5566,#a9b2c0 50%,#3c4656)" role="img" aria-label="Photograph of rolled steel coils">
  <h3>FLAT ROLLED PRODUCTS</h3><p>Lorem Ipsum is simply dummy text</p><a class="btn">SHOP NOW</a>
</article>
<article class="product" style="left:610px;top:1151px;background:linear-gradient(150deg,#3e3b3a,#7d7570 45%,#4a4543)" role="img" aria-label="Photograph of steel reinforcing bars">
  <h3>REINFORCING BAR</h3><p>Lorem Ipsum is simply dummy text</p><a class="btn">SHOP NOW</a>
</article>

<section class="welcome">
  <h2>WELCOME TO QMR</h2>
  <p>The company source and supply various steel and metal products within our international network also manage all aspects of the supply process from point of manufacture to point of delivery. the goal is to create value within the supply chain by building strong supplier, customers and service providers, funding of both customers and suppliers, experienced risk management, efficient document handling.</p>
  <a class="btn" style="left:134px;top:365px;width:106px;height:32px;font-size:12px">READ MORE</a>
  <div class="video" role="img" aria-label="Video showing steel coil being rolled in a mill">
    <svg width="74" height="74" viewBox="0 0 74 74"><circle cx="37" cy="37" r="33" fill="rgba(0,0,0,.25)" stroke="#fff" stroke-width="4"/><path d="M29 22l24 15-24 15z" fill="#fff"/></svg>
  </div>
</section>

<section class="trading" role="img" aria-label="Dark photograph of stacked round steel bars">
  <h2>STEEL TRADING</h2>
  <div class="sec-rule" style="top:140px"></div>
  <p>Lorem ipsum dolor sit amet consectetur adipiscing elit sed<br>do eiusmod tempor incididunt ut labore et dolore magna aliqua<br>Ut enim ad minim veniam quis nostrud exercitation ullamco</p>
  <a class="btn" style="left:533px;top:306px;width:132px;height:41px;font-size:15px">READ MORE</a>
</section>

<h2 class="sec-title" style="top:2469px">SPECIFICATIONS</h2>
<div class="sec-rule" style="top:2516px"></div>
<div class="tabs">
  <div class="tab on" style="left:300px;width:109px">LSAW PIPE</div>
  <div class="tab" style="left:426px;width:101px">ERW PIPE</div>
  <div class="tab" style="left:549px;width:176px">FLAT ROLLED PRODUCTS</div>
  <div class="tab" style="left:745px;width:153px">REINFORCING BAR</div>
</div>
<table class="spec">
  <colgroup><col style="width:173px"><col style="width:290px"><col style="width:230px"><col style="width:238px"></colgroup>
  <tr><th>GRADE</th><th>YIELD STRENGTH, MIN, PSI</th><th>THICKNESSES</th><th>MINIMUM ELONGATION</th></tr>
  <tr><td>WPHY-42</td><td>42,000</td><td>42,000</td><td>25</td></tr>
  <tr><td>WPHY-46</td><td>46,000</td><td>46,000</td><td>65</td></tr>
  <tr><td>WPHY-52</td><td>52,000</td><td>52,000</td><td>25</td></tr>
  <tr><td>WPHY-56</td><td>56,000</td><td>56,000</td><td>25</td></tr>
  <tr><td>WPHY-60</td><td>60,000</td><td>60,000</td><td>20</td></tr>
  <tr><td>WPHY-65</td><td>52,000</td><td>52,000</td><td>45</td></tr>
  <tr><td>WPHY-70</td><td>56,000</td><td>56,000</td><td>85</td></tr>
</table>

<section class="blog">
  <h2 class="sec-title" style="top:41px">LATEST BLOG</h2>
  <div class="sec-rule" style="top:88px"></div>
  <article class="post" style="left:132px">
    <div class="photo" style="background:linear-gradient(135deg,#9aa0a6,#d8dbde 50%,#6f757b)" role="img" aria-label="Photograph of shiny steel coils in a warehouse"></div>
    <h4>LOREM IPSUM DOLOR SIT AMET CONSECTETUR ADIPISCING</h4>
    <p>At vero eos et accusamus et iusto odio dignissimos ducimus qui blanditiis praesentium voluptatum</p>
    <a class="btn">READ MORE</a>
  </article>
  <article class="post" style="left:451px">
    <div class="photo" style="background:linear-gradient(135deg,#4b5a6a,#d9c34a 50%,#3d4a58)" role="img" aria-label="Photograph of a worker in safety gear inspecting steel stock"></div>
    <h4>LOREM IPSUM DOLOR SIT AMET CONSECTETUR ADIPISCING</h4>
    <p>At vero eos et accusamus et iusto odio dignissimos ducimus qui blanditiis praesentium voluptatum</p>
    <a class="btn">READ MORE</a>
  </article>
  <article class="post" style="left:770px">
    <div class="photo" style="background:linear-gradient(135deg,#5a6470,#b07a4a 50%,#3e4650)" role="img" aria-label="Photograph of stacked steel channel beams"></div>
    <h4>LOREM IPSUM DOLOR SIT AMET CONSECTETUR ADIPISCING</h4>
    <p>At vero eos et accusamus et iusto odio dignissimos ducimus qui blanditiis praesentium voluptatum</p>
    <a class="btn">READ MORE</a>
  </article>
</section>

<section class="cta" role="img" aria-label="Abstract dark blue background">
  <h2>ON THE OTHER HAND, WE DENOUNCE WITH<br>RIGHTEOUS INDIGNATION AND DISLIKE MEN<br>WHO ARE SO BEGUILED AND.</h2>
  <a class="btn" style="left:898px;top:93px;width:170px;height:51px;font-size:17px">CONTACT US</a>
</section>

<footer class="footer">
  <div class="brand"><i></i>QMR</div>
  <h5 style="left:424px">MENU</h5>
  <ul class="fmenu"><li>HOME</li><li>ABOUT US</li><li>PRODUCTS</li><li>SERVICES</li><li>BLOG</li><li>CONTACT US</li></ul>

  <h5 style="left:647px">CONTACT US</h5>
  <div class="fitem" style="left:679px;top:89px"><i><svg width="10" height="12" viewBox="0 0 10 12"><path d="M5 0a4 4 0 0 1 4 4c0 3-4 8-4 8S1 7 1 4a4 4 0 0 1 4-4z" fill="#222"/><circle cx="5" cy="4" r="1.5" fill="#fff"/></svg></i>220 Harbour Road<br>Port Vale 3015</div>
  <div class="fitem" style="left:679px;top:140px"><i><svg width="11" height="11" viewBox="0 0 24 24"><path d="M5 3h4l2 5-2.5 1.5a11 11 0 0 0 6 6L16 13l5 2v4a2 2 0 0 1-2 2A17 17 0 0 1 3 5a2 2 0 0 1 2-2z" fill="#222"/></svg></i>Call Us<br>555.014.2290</div>
  <div class="fitem" style="left:679px;top:192px"><i><svg width="12" height="9" viewBox="0 0 12 9"><rect width="12" height="9" fill="#222"/><path d="M0 0l6 5 6-5" stroke="#fff" fill="none"/></svg></i>E mail Us<br>info@qmr.com</div>

  <h5 style="left:963px">FOLLOW US</h5>
  <div class="fitem" style="left:998px;top:89px"><i></i>Like us on<br>CHATTERLY</div>
  <div class="fitem" style="left:998px;top:140px"><i></i>Follow us on<br>CHIRPLINE</div>
  <div class="fitem" style="left:998px;top:192px"><i></i>Follow us on<br>WORKNET</div>

  <hr>
  <p class="copy">Copyright © 2020 All Rights Reserved</p>
</footer>

</body>
</html>
```